LinkedIn Cover Image

We need a Linked In Cover Image for our Linked In Business Page.

The dimensions needed are: 1536 x 768px.

Here's a link to our website: www.harborvalerepair.com
LinkedIn Profile: https://www.linkedin.com/company/harborvale-repair-services/

Font styles to use
Sans Serif

Colors

Designer to choose colors to be used in the design.

```html
<!DOCTYPE html>
<html lang="en">
<head>
<meta charset="utf-8">
<title>Harborvale Repair Services – LinkedIn Cover</title>
<link rel="stylesheet" href="https://fonts.googleapis.com/css2?family=Montserrat:wght@600;700&display=swap">
<style>
  :root {
    --teal-deep: #4f737b;
    --teal-mid: #6a8d94;
    --teal-light: #86a5aa;
    --orange: #f28a1f;
    --orange-soft: #f7a450;
    --white: #ffffff;
    --star-fill: #e9e9ea;
    --ink: #2f3a3d;
  }
  html, body {
    margin: 0;
    padding: 0;
    overflow: hidden;
    background: var(--teal-deep);
  }
  .cover {
    position: relative;
    width: 1200px;
    height: 600px;
    overflow: hidden;
    font-family: "Montserrat", Arial, sans-serif;
  }
  .cover__backdrop {
    position: absolute;
    inset: 0;
    background:
      linear-gradient(180deg, rgba(60,90,97,0.55) 0%, rgba(60,90,97,0) 35%),
      linear-gradient(90deg, var(--teal-deep) 0%, var(--teal-mid) 45%, var(--teal-light) 75%, var(--teal-mid) 100%);
  }
  .cover__art {
    position: absolute;
    inset: 0;
  }
  .route { fill: none; stroke: var(--orange); stroke-width: 4; stroke-linejoin: round; }
  .route-dot { fill: var(--orange); }
  .service-ring { fill: rgba(79,115,123,0.35); stroke: var(--orange); stroke-width: 5; }
  .service-ring--star { fill: var(--star-fill); }
  .service-icon { fill: var(--orange); }
  .service-icon__shine { fill: var(--orange-soft); }
  .star-icon { fill: none; stroke: var(--ink); stroke-width: 3; stroke-linejoin: round; }
  .brand-name {
    font-family: "Montserrat", Arial, sans-serif;
    font-weight: 700;
    fill: var(--orange);
  }
  .headline {
    font-family: "Montserrat", Arial, sans-serif;
    font-weight: 600;
    fill: var(--white);
    font-size: 92px;
  }
</style>
</head>
<body>
<main class="cover">
  <div class="cover__backdrop" role="img" aria-label="Photograph of an empty warehouse interior with steel roof trusses and concrete floor, tinted teal"></div>

  <svg class="cover__art" width="1200" height="600" viewBox="0 0 1200 600" xmlns="http://www.w3.org/2000/svg">
    <defs>
      <filter id="soft-shadow" x="-30%" y="-30%" width="160%" height="160%">
        <feDropShadow dx="0" dy="3" stdDeviation="4" flood-color="#1d2b2e" flood-opacity="0.45"/>
      </filter>
    </defs>

    <!-- service route -->
    <polyline class="route" points="312,76 120,220 60,392 184,512 662,482 960,520 1112,356 928,116"/>
    <circle class="route-dot" cx="312" cy="76" r="16"/>
    <circle class="route-dot" cx="928" cy="116" r="16"/>

    <!-- water damage -->
    <g class="service service--water" filter="url(#soft-shadow)">
      <circle class="service-ring" cx="120" cy="220" r="56"/>
      <path class="service-icon" d="M120,184 C128,204 144,222 144,240 C144,254 133,264 120,264 C107,264 96,254 96,240 C96,222 112,204 120,184 Z"/>
      <path class="service-icon__shine" d="M120,212 C125,224 134,234 134,244 C134,252 128,258 120,258 C112,258 106,252 106,244 C106,234 115,224 120,212 Z"/>
    </g>

    <!-- fire damage -->
    <g class="service service--fire" filter="url(#soft-shadow)">
      <circle class="service-ring" cx="184" cy="512" r="56"/>
      <path class="service-icon" d="M186,470 C190,486 208,496 208,520 C208,538 197,550 184,550 C170,550 160,538 160,522 C160,506 170,498 172,486 C178,494 180,500 180,506 C186,496 188,484 186,470 Z"/>
      <path class="service-icon__shine" d="M186,508 C190,518 198,524 198,534 C198,542 192,548 185,548 C178,548 172,542 172,534 C172,524 182,518 186,508 Z"/>
    </g>

    <!-- mold & air quality -->
    <g class="service service--air" filter="url(#soft-shadow)">
      <circle class="service-ring" cx="662" cy="482" r="58"/>
      <path class="service-icon" d="M648,452 L676,452 C684,462 688,476 686,492 C684,504 674,512 662,512 C650,512 640,504 638,492 C636,476 640,462 648,452 Z"/>
      <rect class="service-icon__shine" x="653" y="478" width="18" height="14" rx="3"/>
      <circle class="service-icon" cx="633" cy="504" r="15"/>
      <circle class="service-icon" cx="691" cy="504" r="15"/>
      <circle class="service-icon__shine" cx="633" cy="504" r="8"/>
      <circle class="service-icon__shine" cx="691" cy="504" r="8"/>
    </g>

    <!-- quality promise -->
    <g class="service service--star" filter="url(#soft-shadow)">
      <circle class="service-ring service-ring--star" cx="1112" cy="356" r="60"/>
      <polygon class="star-icon" points="1112,316 1122,345 1152,345 1128,363 1137,392 1112,374 1087,392 1096,363 1072,345 1102,345"/>
    </g>

    <!-- brand name -->
    <g class="brand" filter="url(#soft-shadow)">
      <text class="brand-name" x="602" y="102" text-anchor="middle" font-size="64" textLength="380" lengthAdjust="spacingAndGlyphs">HARBORVALE</text>
      <text class="brand-name" x="602" y="144" text-anchor="middle" font-size="30" textLength="380" lengthAdjust="spacingAndGlyphs">REPAIR SERVICES</text>
    </g>

    <!-- headline -->
    <g class="headline-group" filter="url(#soft-shadow)">
      <text class="headline" x="582" y="284" text-anchor="middle" textLength="636" lengthAdjust="spacingAndGlyphs">GETTING YOU</text>
      <text class="headline" x="592" y="388" text-anchor="middle" textLength="824" lengthAdjust="spacingAndGlyphs">BACK TO NORMAL</text>
    </g>
  </svg>
</main>
</body>
</html>
```